I dont have a logo yet. My mind in color is navy blue and khaki maybe a tiny bit of yellow but open to ideas. name of the business is Prairie Ridge Builders. Dedicated to all sorts of construction commerical and residential. Im Tomas Verdugo owner of business<br/>Address to business is 287 N. Marbury El Paso Tx 79925 <br/>Phone is 9156820374<br/>Id like round corners i also like the see thru card a little.<br/>Open to trademark quotes

Target Market(s)

Construction

Contact Information for Business Card

PRAIRIE RIDGE BUILDERS LLC

Tomas Verdugo
Director of Operations

Commercial & Residential

9156820374
PRAIRIE.R.BUILDERS@MAILHAVEN.NET

Colors
0355a3
fff3d1

Requirements
Must have
• ROUND CORNERS
• BLUE AND KHAKI AND CLEAR
• LOGO

```html
<!DOCTYPE html>
<html lang="en">
<head>
<meta charset="utf-8">
<title>Prairie Ridge Builders – Business Card</title>
<link rel="stylesheet" href="https://fonts.googleapis.com/css2?family=Cinzel:wght@500;600&family=Tinos:wght@400&display=swap">
<style>
  :root {
    --navy: #2c2a86;
    --navy-deep: #24236f;
    --khaki: #c7ac86;
    --white: #ffffff;
    --silver: #d4d6df;
    --stage: #2a2a2c;
  }
  * { margin: 0; padding: 0; box-sizing: border-box; }
  html, body { width: 1200px; height: 1200px; overflow: hidden; background: var(--stage); }
  .canvas { position: relative; width: 1200px; height: 1200px; }

  .card {
    position: absolute; left: 150px; width: 900px; height: 514px;
    border-radius: 30px; overflow: hidden;
  }
  .card-back { top: 50px; background: var(--navy); }
  .card-front { top: 630px; background: var(--white); }

  .back-brand {
    position: absolute; left: 0; right: 0; top: 0; bottom: 0;
    display: flex; align-items: center; justify-content: center; gap: 22px;
  }
  .brand-dot { width: 74px; height: 74px; border-radius: 50%; background: var(--silver); flex: none; }
  .brand-dot.navy { background: var(--navy); width: 78px; height: 78px; }
  .brand-name {
    font-family: "Cinzel", serif; font-weight: 600; color: var(--silver);
    font-size: 50px; line-height: 1.05; letter-spacing: 1px;
  }

  .front-art { position: absolute; inset: 0; }

  .front-brand {
    position: absolute; left: 60px; top: 52px;
    display: flex; align-items: center; gap: 20px;
  }
  .front-brand .brand-name { color: var(--navy); font-size: 46px; }

  .person { position: absolute; left: 60px; top: 210px; font-family: "Cinzel", serif; }
  .person-name { color: var(--navy); font-size: 32px; font-weight: 600; letter-spacing: 1px; }
  .person-role { color: var(--khaki); font-size: 21px; font-weight: 500; letter-spacing: 1px; margin-top: 2px; }
  .divider { position: absolute; left: 60px; top: 292px; width: 600px; height: 2px; background: var(--khaki); }

  .contacts { position: absolute; left: 60px; top: 306px; list-style: none; font-family: "Tinos", serif; color: var(--navy-deep); font-size: 20px; }
  .contacts li { display: flex; align-items: center; gap: 10px; height: 30px; }
  .contact-icon { width: 20px; height: 20px; flex: none; }

  .tagline, .services {
    position: absolute; left: 36px; font-family: "Tinos", serif; font-weight: 400;
    text-transform: uppercase; letter-spacing: 1px;
  }
  .tagline { top: 422px; color: var(--white); font-size: 22px; }
  .services { top: 468px; color: var(--white); font-size: 22px; }
</style>
</head>
<body>
<main class="canvas">

  <section class="card card-back" aria-label="Card back">
    <div class="back-brand">
      <span class="brand-dot" aria-hidden="true"></span>
      <h1 class="brand-name">PRAIRIE RIDGE<br>BUILDERS</h1>
    </div>
  </section>

  <section class="card card-front" aria-label="Card front">
    <svg class="front-art" width="900" height="514" viewBox="0 0 900 514" aria-hidden="true">
      <polygon points="620,514 900,514 900,110 840,110" fill="var(--khaki)"/>
      <polygon points="0,412 540,412 575,456 0,456" fill="var(--navy)"/>
      <polygon points="0,456 575,456 620,514 0,514" fill="var(--khaki)"/>
      <circle cx="640" cy="468" r="34" fill="var(--navy)"/>
      <path d="M622 470 L640 454 L658 470 L653 470 L653 484 L627 484 L627 470 Z" fill="var(--white)"/>
      <circle cx="726" cy="468" r="34" fill="var(--navy)"/>
      <rect x="712" y="450" width="22" height="34" fill="var(--white)"/>
      <rect x="734" y="462" width="10" height="22" fill="var(--silver)"/>
      <g fill="var(--navy)">
        <rect x="716" y="455" width="5" height="5"/><rect x="725" y="455" width="5" height="5"/>
        <rect x="716" y="465" width="5" height="5"/><rect x="725" y="465" width="5" height="5"/>
        <rect x="716" y="475" width="5" height="5"/><rect x="725" y="475" width="5" height="5"/>
      </g>
    </svg>

    <div class="front-brand">
      <span class="brand-dot navy" aria-hidden="true"></span>
      <h2 class="brand-name">PRAIRIE RIDGE<br>BUILDERS</h2>
    </div>

    <div class="person">
      <p class="person-name">TOMAS VERDUGO</p>
      <p class="person-role">DIRECTOR OF OPERATIONS</p>
    </div>
    <div class="divider"></div>

    <ul class="contacts">
      <li>
        <svg class="contact-icon" viewBox="0 0 20 20"><circle cx="10" cy="10" r="10" fill="var(--khaki)"/><path d="M6.5 5.5 L8.5 5.5 L9.3 8 L8 9 Q9 11.2 11 12 L12 10.7 L14.5 11.5 L14.5 13.5 Q10 14.5 7.5 11.5 Q5.5 9 6.5 5.5 Z" fill="var(--white)"/></svg>
        9156820374
      </li>
      <li>
        <svg class="contact-icon" viewBox="0 0 20 20"><circle cx="10" cy="10" r="10" fill="var(--khaki)"/><rect x="5" y="6.5" width="10" height="7" fill="none" stroke="var(--white)" stroke-width="1.3"/><path d="M5 6.5 L10 10.5 L15 6.5" fill="none" stroke="var(--white)" stroke-width="1.3"/></svg>
        PRAIRIE.R.BUILDERS@MAILHAVEN.NET
      </li>
      <li>
        <svg class="contact-icon" viewBox="0 0 20 20"><circle cx="10" cy="10" r="10" fill="var(--khaki)"/><path d="M10 15.5 Q6 11 6 8.5 A4 4 0 0 1 14 8.5 Q14 11 10 15.5 Z" fill="var(--white)"/><circle cx="10" cy="8.5" r="1.5" fill="var(--khaki)"/></svg>
        287 N. Marbury El Paso Tx 79925
      </li>
    </ul>

    <p class="tagline">Dedicated to the American Dream</p>
    <p class="services">Commerical and Residential</p>
  </section>

</main>
</body>
</html>
```